Business card and stationary for a Massage Therapist
Kneading Haven Studio
Business card and stationary for a Massage Therapist - Massage Therapy
Creative Brief
Professional
Gwen Holloway M.S., L.M.T
Orchard Commons 412 Rte. 9B Alderbrook, VT 05901
studio@fernwickmail.com
www.kneadinghavenstudio.com

```html
<!DOCTYPE html>
<html lang="en">
<head>
<meta charset="utf-8">
<title>Kneading Haven Studio – Business Card</title>
<link href="https://fonts.googleapis.com/css2?family=Lato:wght@300;400&display=swap" rel="stylesheet">
<style>
  :root {
    --backdrop: #e6e8e9;
    --card: #b7ccd7;
    --card-band: #a2b8c4;
    --band-edge: #93aab7;
    --ink: #667c89;
    --ink-soft: #7b909c;
    --band-ink: #eef4f7;
  }
  * { margin: 0; padding: 0; box-sizing: border-box; }
  html, body {
    width: 1200px; height: 904px; overflow: hidden;
    background: var(--backdrop);
    font-family: "Lato", sans-serif;
  }
  .stage {
    width: 1200px; height: 904px;
    display: flex; flex-direction: column;
    align-items: center; justify-content: center; gap: 40px;
  }
  .card {
    position: relative;
    width: 700px; height: 400px;
    background: var(--card);
    box-shadow: 0 2px 10px rgba(0,0,0,.12);
    overflow: hidden;
  }
  .card-back {
    display: flex; align-items: center; justify-content: center;
  }
  .brand {
    display: flex; align-items: center; gap: 12px;
    color: var(--ink);
    font-weight: 400;
    white-space: nowrap;
  }
  .brand-dot {
    width: 20px; height: 20px; border-radius: 50%;
    background: var(--ink);
    flex-shrink: 0;
  }
  .card-back .brand-name { font-size: 30px; letter-spacing: 1px; }

  .card-front .brand {
    position: absolute; left: 56px; top: 176px;
  }
  .card-front .brand-name { font-size: 22px; letter-spacing: .3px; }
  .contact {
    position: absolute; left: 400px; top: 70px;
    color: var(--ink);
    font-weight: 300;
  }
  .contact .person {
    font-size: 19px; font-weight: 400; margin-bottom: 18px;
  }
  .contact .address p { font-size: 14px; line-height: 21px; }
  .contact .lines { margin-top: 18px; }
  .contact .line {
    display: flex; align-items: center; gap: 10px;
    font-size: 14px; line-height: 22px;
  }
  .contact .line svg { width: 13px; height: 13px; fill: var(--ink); flex-shrink: 0; }
  .web-band {
    position: absolute; left: 0; right: 0; bottom: 0;
    height: 52px;
    background: var(--card-band);
    border-top: 3px solid var(--band-edge);
    display: flex; align-items: center; justify-content: center;
    color: var(--band-ink);
    font-size: 15px; letter-spacing: 3px; font-weight: 300;
  }
</style>
</head>
<body>
<main class="stage">
  <section class="card card-back" aria-label="Card back">
    <div class="brand">
      <span class="brand-dot"></span>
      <span class="brand-name">Kneading Haven Studio</span>
    </div>
  </section>

  <section class="card card-front" aria-label="Card front">
    <div class="brand">
      <span class="brand-dot"></span>
      <span class="brand-name">Kneading Haven Studio</span>
    </div>

    <div class="contact">
      <p class="person">Gwen Holloway M.S., L.M.T</p>
      <div class="address">
        <p>Orchard Commons</p>
        <p>412 Rte. 9B</p>
        <p>Alderbrook, VT 05901</p>
      </div>
      <div class="lines">
        <p class="line">
          <svg viewBox="0 0 24 24" aria-hidden="true"><path d="M6.6 10.8a15.1 15.1 0 0 0 6.6 6.6l2.2-2.2a1 1 0 0 1 1-.25 11.4 11.4 0 0 0 3.6.57 1 1 0 0 1 1 1V20a1 1 0 0 1-1 1A17 17 0 0 1 3 4a1 1 0 0 1 1-1h3.5a1 1 0 0 1 1 1c0 1.25.2 2.45.57 3.57a1 1 0 0 1-.25 1z"/></svg>
          508.555.0142
        </p>
        <p class="line">
          <svg viewBox="0 0 24 24" aria-hidden="true"><path d="M2 5h20v14H2zm2 2v.4l8 5 8-5V7zm0 2.8V17h16V9.8l-8 5z"/></svg>
          studio@fernwickmail.com
        </p>
      </div>
    </div>

    <div class="web-band">www.kneadinghavenstudio.com</div>
  </section>
</main>
</body>
</html>
```